Copper Lark Treks Flyer

I have an adventure travel company and I need a flyer to promote my trip to Ukraine.
I would like to have a universal flyer that I can change based on the trip.
The Title should say "Travel to Ukraine: 9 Day Eastern European Adventure"
The date should be under the title.
The background photo should be kiev2.jpg
The highlights of the trip, then price $1200 and what it includes. See the text for highlights and includes sections here:
http://www.copperlarktreks.com/#!featured-trip
The website link (www.copperlarktreks.com) should be somewhere in the bottom.
You can use other photos provided or from my website that relates to Ukraine trip.

```html
<!DOCTYPE html>
<html lang="en">
<head>
<meta charset="utf-8">
<title>Copper Lark Treks – Travel to Ukraine</title>
<link rel="stylesheet" href="https://fonts.googleapis.com/css2?family=Alfa+Slab+One&family=PT+Sans:wght@400;700&display=swap">
<style>
  :root {
    --red: #e11d2a;
    --yellow: #fff200;
    --yellow-soft: #ffe24a;
    --sky: #00aeef;
    --white: #ffffff;
    --ink: #1a1a1a;
    --display: "Alfa Slab One", serif;
    --body: "PT Sans", sans-serif;
  }
  * { box-sizing: border-box; margin: 0; padding: 0; }
  html, body { width: 933px; height: 1200px; overflow: hidden; background: var(--white); }
  .flyer { position: relative; width: 933px; height: 1200px; overflow: hidden; font-family: var(--body); }
  .backdrop { position: absolute; inset: 0; }

  .photo { position: absolute; border: 6px solid var(--white); box-shadow: 0 2px 6px rgba(0,0,0,.45); }
  .photo--lavra { left: 36px; top: 0; width: 154px; height: 112px; transform: rotate(-6deg);
    background: linear-gradient(180deg,#b9cde0 0%,#d8c27a 45%,#6d7f55 100%); }
  .photo--cave { left: 712px; top: 70px; width: 175px; height: 140px; transform: rotate(6deg);
    background: radial-gradient(circle at 50% 40%,#e2c9a0 0%,#9a6a3c 55%,#3b2414 100%); }
  .photo--tram { left: 75px; top: 518px; width: 208px; height: 132px;
    background: linear-gradient(180deg,#c9cfd2 0%,#8d8a80 55%,#5c5048 100%); }
  .photo--peaks { left: 375px; top: 518px; width: 207px; height: 132px;
    background: linear-gradient(180deg,#c4d3e0 0%,#8f9aa3 55%,#4f5a3d 100%); }
  .photo--coast { left: 652px; top: 518px; width: 196px; height: 132px;
    background: linear-gradient(180deg,#4c6c8c 0%,#5d8fb0 45%,#4f7240 100%); }

  .title { position: absolute; z-index: 2; left: 54px; top: 80px; width: 720px; transform: rotate(-7.8deg);
    text-align: center; color: var(--yellow); font-family: var(--display); }
  .title__text { font-size: 36px; line-height: 1.08; font-weight: 400; letter-spacing: .5px;
    text-shadow: 1px 1px 0 rgba(0,0,0,.25); }
  .title__dates { margin-top: 2px; font-family: var(--body); font-weight: 700; font-size: 18px; color: var(--white); }

  .price { position: absolute; left: 54px; top: 178px; width: 130px; height: 130px; border-radius: 50%;
    background: var(--yellow); border: 4px solid var(--red); box-shadow: 0 0 0 3px var(--yellow);
    display: flex; flex-direction: column; align-items: center; justify-content: center;
    color: var(--red); font-family: var(--display); transform: rotate(-10deg); line-height: 1; }
  .price__label { font-size: 22px; }
  .price__amount { font-size: 30px; margin-top: 4px; }

  .details { position: absolute; left: 72px; top: 661px; width: 845px; color: var(--white); }
  .details__heading { font-family: var(--display); font-size: 17px; color: var(--yellow-soft);
    letter-spacing: .5px; line-height: 1; margin-bottom: 2px; }
  .highlights { list-style: none; font-size: 14.5px; line-height: 21px; }
  .highlights li { position: relative; padding-left: 18px; white-space: nowrap; }
  .highlights li svg { position: absolute; left: 0; top: 5px; }
  .accent { color: var(--yellow-soft); }
  .included { margin-top: 7px; padding-left: 6px; }
  .included__list { list-style: none; font-size: 14.5px; line-height: 21.3px; margin-top: 2px; }
  .included__list li::before { content: "•"; color: var(--yellow-soft); margin-right: 6px; }

  .contact { position: absolute; left: 0; top: 925px; width: 933px; height: 72px; background: var(--sky); }
  .contact__person { position: absolute; left: 50px; top: 10px; font-size: 15px; line-height: 18px; }
  .contact__name { color: var(--yellow-soft); font-weight: 700; }
  .contact__email { color: var(--white); font-weight: 700; }
  .contact__email span { color: var(--yellow-soft); }
  .contact__fax { color: var(--ink); font-weight: 700; }
  .contact__main { position: absolute; right: 48px; top: 6px; text-align: center; color: var(--yellow); }
  .contact__phone { font-family: var(--display); font-size: 31px; line-height: 1.1; }
  .contact__web { font-family: var(--display); font-size: 17px; }

  .tabs { position: absolute; left: 0; top: 1000px; width: 933px; height: 200px; display: flex; gap: 3px; padding-left: 3px; }
  .tab { flex: 1; background: var(--sky); display: flex; justify-content: center; padding-top: 10px; }
  .tab__text { writing-mode: vertical-rl; color: var(--yellow-soft); font-weight: 700; font-size: 13px; line-height: 22px; }
</style>
</head>
<body>
<main class="flyer">
  <svg class="backdrop" width="933" height="1200" viewBox="0 0 933 1200">
    <defs>
      <linearGradient id="lavraTones" x1="0" y1="0" x2="0" y2="1">
        <stop offset="0" stop-color="#6f8a5a"/>
        <stop offset=".35" stop-color="#c9a23a"/>
        <stop offset=".7" stop-color="#8a8478"/>
        <stop offset="1" stop-color="#5e7a4c"/>
      </linearGradient>
    </defs>
    <polygon points="0,100 933,0 933,917 0,917" fill="var(--red)"/>
    <polygon points="0,262 933,160 933,617 0,617" fill="url(#lavraTones)" role="img" aria-label="Aerial photo of the golden-domed Kyiv Pechersk Lavra among green trees"/>
    <rect x="0" y="613" width="933" height="8" fill="var(--sky)"/>
  </svg>

  <div class="photo photo--lavra" role="img" aria-label="Photo of monastery domes in Kyiv"></div>
  <div class="photo photo--cave" role="img" aria-label="Photo of a limestone cave with stalactites"></div>

  <header class="title">
    <h1 class="title__text">Travel to Ukraine: 9 Day Eastern<br>European Adventure</h1>
    <p class="title__dates">Fri May 18 - &nbsp;Sun May 27</p>
  </header>

  <div class="price"><span class="price__label">PRICE</span><span class="price__amount">$1200</span></div>

  <div class="photo photo--tram" role="img" aria-label="Photo of a red tram on a tree-lined city street"></div>
  <div class="photo photo--peaks" role="img" aria-label="Photo of a pine tree before snowy Crimean mountains"></div>
  <div class="photo photo--coast" role="img" aria-label="Photo of the green Yalta coastline and the Black Sea"></div>

  <section class="details">
    <h2 class="details__heading">HIGHLIGHTS:</h2>
    <ul class="highlights">
      <li><svg width="14" height="11" viewBox="0 0 14 11"><path d="M1 6 L5 10 L13 1" stroke="var(--yellow-soft)" stroke-width="2" fill="none"/></svg>Discover <span class="accent">Kiev</span>- the birthplace of Eastern Slavic Civilization</li>
      <li><svg width="14" height="11" viewBox="0 0 14 11"><path d="M1 6 L5 10 L13 1" stroke="var(--yellow-soft)" stroke-width="2" fill="none"/></svg>Meet <span class="accent">Crimea's</span> fascinating <span class="accent">Tatar</span> Minority in Bakhchysaray - former capital of Crimean Tatar Khans</li>
      <li><svg width="14" height="11" viewBox="0 0 14 11"><path d="M1 6 L5 10 L13 1" stroke="var(--yellow-soft)" stroke-width="2" fill="none"/></svg>Walk to <span class="accent">Chufut-Kale</span> - Crimea's best preserved &nbsp;medieval cave town</li>
      <li><svg width="14" height="11" viewBox="0 0 14 11"><path d="M1 6 L5 10 L13 1" stroke="var(--yellow-soft)" stroke-width="2" fill="none"/></svg><span class="accent">Hike</span> in the most spectacular areas in Karabi and &nbsp;&nbsp;with a group of professional speleologist</li>
      <li><svg width="14" height="11" viewBox="0 0 14 11"><path d="M1 6 L5 10 L13 1" stroke="var(--yellow-soft)" stroke-width="2" fill="none"/></svg>Inhale the magic <span class="accent">Yalta's air</span>- an invigorating blend of sea and pine forest sprinkled with mountain chill</li>
      <li><svg width="14" height="11" viewBox="0 0 14 11"><path d="M1 6 L5 10 L13 1" stroke="var(--yellow-soft)" stroke-width="2" fill="none"/></svg>Visit <span class="accent">Odessa</span>- "the Pearl by the Black Sea", Catacombs, Opera house, the factory of sparkling wines and famous <span class="accent">Potemkin Steps</span></li>
    </ul>
    <div class="included">
      <h2 class="details__heading">INCLUDED:</h2>
      <ul class="included__list">
        <li>9 nights accommodations</li>
        <li>Breakfast, lunch and dinner daily</li>
        <li>English speaking guides at every destination.</li>
        <li>All Local Transfers (trains, buses and vans), &nbsp;sightseeing tours and entrance fees</li>
      </ul>
    </div>
  </section>

  <footer class="contact">
    <div class="contact__person">
      <p class="contact__name">Marta Velichko</p>
      <p class="contact__email">Email: <span>marta@copperlarktreks.com</span></p>
      <p class="contact__fax">Fax # 555-014-2731</p>
    </div>
    <div class="contact__main">
      <p class="contact__phone">1.555.014.2730</p>
      <p class="contact__web">www.copperlarktreks.com</p>
    </div>
  </footer>

  <div class="tabs">
    <div class="tab"><p class="tab__text">1.555.014.2730<br>www.copperlarktreks.com</p></div>
    <div class="tab"><p class="tab__text">1.555.014.2730<br>www.copperlarktreks.com</p></div>
    <div class="tab"><p class="tab__text">1.555.014.2730<br>www.copperlarktreks.com</p></div>
    <div class="tab"><p class="tab__text">1.555.014.2730<br>www.copperlarktreks.com</p></div>
    <div class="tab"><p class="tab__text">1.555.014.2730<br>www.copperlarktreks.com</p></div>
    <div class="tab"><p class="tab__text">1.555.014.2730<br>www.copperlarktreks.com</p></div>
    <div class="tab"><p class="tab__text">1.555.014.2730<br>www.copperlarktreks.com</p></div>
    <div class="tab"><p class="tab__text">1.555.014.2730<br>www.copperlarktreks.com</p></div>
    <div class="tab"><p class="tab__text">1.555.014.2730<br>www.copperlarktreks.com</p></div>
    <div class="tab"><p class="tab__text">1.555.014.2730<br>www.copperlarktreks.com</p></div>
  </div>
</main>
</body>
</html>
```